Brightwell Power "Unique Process" Graphic

Create a "graphic" that creatively represents the seven-step process that Brightwell Power uses to serve our customers.
This graphic should be sized in such a way that it can easily be included on a page in our website, and also used in other marketing materials such as flyers, emails and powerpoint presentations.
As an EXAMPLE of a similar graphic, see the "Proven Process" section of the home page of this website - https://www.northvanetek.example/
I'll include our brand documentation as well as the document for our "Unique Process" in the uploaded files section.
Please use our brand colors and also be creative in how you represent the seven steps graphically.
Here's a bit about our business.
Brightwell Power is one of the largest B2B Energy Brokers in the US. We serve tens of thousands of customers by securing energy contracts for them. We are NOT an energy company ourselves - but a broker that represents 30+ energy suppliers to commercial and nonprofit customers.

```html
<!DOCTYPE html>
<html lang="en">
<head>
<meta charset="utf-8">
<title>Brightwell Power – Brightwell Difference</title>
<link rel="stylesheet" href="https://fonts.googleapis.com/css2?family=Montserrat:ital,wght@0,600;0,700;0,800;1,800&family=Lato:wght@400;700&display=swap">
<style>
  :root {
    --green: #1a9a3e;
    --navy: #0b2d6b;
    --path: #bdbdbd;
    --badge: #c6c6c6;
    --paper: #ffffff;
    --ink-light: #ffffff;
  }
  html, body {
    margin: 0;
    width: 1200px;
    height: 920px;
    overflow: hidden;
    background: var(--paper);
  }
  .process-graphic { display: block; width: 1200px; height: 920px; }
  .brand-name { font-family: "Montserrat", sans-serif; font-weight: 800; font-size: 34px; fill: var(--navy); letter-spacing: 0.5px; }
  .brand-square { fill: var(--green); }
  .step-pill--green { fill: var(--green); }
  .step-pill--navy { fill: var(--navy); }
  .step-disc { fill: var(--paper); }
  .process-path { fill: none; stroke: var(--path); stroke-width: 14; stroke-linecap: butt; }
  .process-arrow { fill: var(--path); }
  .step-label { font-family: "Montserrat", sans-serif; font-weight: 600; font-size: 11px; text-anchor: middle; }
  .step-number { font-family: "Montserrat", sans-serif; font-weight: 700; font-size: 36px; text-anchor: middle; }
  .tone-green { fill: var(--green); }
  .tone-navy { fill: var(--navy); }
  .step-copy { font-family: "Lato", sans-serif; font-size: 9.4px; fill: var(--ink-light); }
  .step-copy--end { text-anchor: end; }
  .badge-shape { fill: var(--badge); }
  .badge-icon { fill: none; stroke: #ffffff; stroke-width: 1.7; stroke-linecap: round; stroke-linejoin: round; }
  .headline { font-family: "Montserrat", sans-serif; font-weight: 800; font-style: italic; font-size: 33px; fill: var(--navy); text-anchor: end; }
</style>
</head>
<body>
<svg class="process-graphic" viewBox="77 80 1000 705" preserveAspectRatio="xMidYMid meet" xmlns="http://www.w3.org/2000/svg">
  <rect x="0" y="0" width="1200" height="900" fill="#ffffff"/>

  <!-- brand -->
  <g class="brand">
    <rect class="brand-square" x="140" y="172" width="48" height="48" rx="4"/>
    <text class="brand-name" x="202" y="208">BRIGHTWELL POWER</text>
  </g>

  <!-- step pills -->
  <g class="pills">
    <rect class="step-pill--navy" x="440" y="622" width="205" height="77" rx="38.5"/>
    <rect class="step-pill--green" x="200" y="512" width="240" height="77" rx="38.5"/>
    <rect class="step-pill--navy" x="510" y="510" width="245" height="77" rx="38.5"/>
    <rect class="step-pill--green" x="310" y="400" width="240" height="77" rx="38.5"/>
    <rect class="step-pill--navy" x="620" y="400" width="245" height="77" rx="38.5"/>
    <rect class="step-pill--green" x="420" y="288" width="240" height="77" rx="38.5"/>
    <rect class="step-pill--navy" x="730" y="288" width="245" height="77" rx="38.5"/>
  </g>

  <!-- step discs -->
  <g class="discs">
    <circle class="step-disc" cx="421" cy="665" r="50"/>
    <circle class="step-disc" cx="421" cy="555" r="50"/>
    <circle class="step-disc" cx="531" cy="555" r="50"/>
    <circle class="step-disc" cx="531" cy="445" r="50"/>
    <circle class="step-disc" cx="641" cy="445" r="50"/>
    <circle class="step-disc" cx="641" cy="335" r="50"/>
    <circle class="step-disc" cx="751" cy="335" r="50"/>
  </g>

  <!-- winding path -->
  <path class="process-path" d="M168,635 L340,635 Q366,635 366,660 L366,665
    A55,55 0 1 0 421,610
    A55,55 0 1 1 476,555
    A55,55 0 1 0 531,500
    A55,55 0 1 1 586,445
    A55,55 0 1 0 641,390
    A55,55 0 1 1 696,335
    A55,55 0 1 0 751,280
    Q735,280 735,262 Q735,242 760,242 L1016,242"/>
  <polygon class="process-arrow" points="1014,228 1031,242 1014,256"/>
  <polygon class="process-arrow" points="148,627 176,627 170,635 176,643 148,643 154,635"/>

  <!-- step labels -->
  <g class="labels">
    <text class="step-label tone-green" x="421" y="640">BRIGHTWELL</text>
    <text class="step-label tone-green" x="421" y="652">ASSESSMENT</text>
    <text class="step-number tone-green" x="421" y="688">01</text>

    <text class="step-label tone-navy" x="421" y="531">BRIGHTWELL</text>
    <text class="step-label tone-navy" x="421" y="543">OPTIONS!</text>
    <text class="step-number tone-navy" x="421" y="579">02</text>

    <text class="step-label tone-green" x="531" y="531">BRIGHTWELL</text>
    <text class="step-label tone-green" x="531" y="543">SIGN-UP!</text>
    <text class="step-number tone-green" x="531" y="579">03</text>

    <text class="step-label tone-navy" x="531" y="421">BRIGHTWELL</text>
    <text class="step-label tone-navy" x="531" y="433">QA</text>
    <text class="step-number tone-navy" x="531" y="469">04</text>

    <text class="step-label tone-green" x="641" y="421">BRIGHTWELL</text>
    <text class="step-label tone-green" x="641" y="433">MONITORING</text>
    <text class="step-number tone-green" x="641" y="469">05</text>

    <text class="step-label tone-navy" x="641" y="311">BRIGHTWELL</text>
    <text class="step-label tone-navy" x="641" y="323">RENEWAL</text>
    <text class="step-number tone-navy" x="641" y="359">06</text>

    <text class="step-label tone-green" x="751" y="311">BRIGHTWELL</text>
    <text class="step-label tone-green" x="751" y="323">GUARANTEE</text>
    <text class="step-number tone-green" x="751" y="359">07</text>
  </g>

  <!-- step copy -->
  <g class="copy">
    <text class="step-copy" x="495" y="641">
      <tspan x="495">Spend 15 minutes with our</tspan>
      <tspan x="495" dy="10.5">team while we analyze your</tspan>
      <tspan x="495" dy="10.5">account and contract details</tspan>
      <tspan x="495" dy="10.5">to select suppliers that fit</tspan>
      <tspan x="495" dy="10.5">your needs.</tspan>
    </text>
    <text class="step-copy step-copy--end" x="355" y="525">
      <tspan x="355">We'll send you an energy quote</tspan>
      <tspan x="355" dy="10.5">with at least three options to</tspan>
      <tspan x="355" dy="10.5">choose from-including different</tspan>
      <tspan x="355" dy="10.5">suppliers and contract terms.</tspan>
      <tspan x="355" dy="10.5">Our unbiased advice will help</tspan>
      <tspan x="355" dy="10.5">you find the best solution!</tspan>
    </text>
    <text class="step-copy" x="607" y="540">
      <tspan x="607">Our simple sign-up process is</tspan>
      <tspan x="607" dy="10.5">handled electronically. Even</tspan>
      <tspan x="607" dy="10.5">contract signatures.</tspan>
    </text>
    <text class="step-copy step-copy--end" x="456" y="424">
      <tspan x="456">Every order detail is</tspan>
      <tspan x="456" dy="10.5">confirmed to ensure</tspan>
      <tspan x="456" dy="10.5">accuracy and smooth</tspan>
      <tspan x="456" dy="10.5">processing.</tspan>
    </text>
    <text class="step-copy" x="717" y="414">
      <tspan x="717">We proactively monitor your</tspan>
      <tspan x="717" dy="10.5">accounts to address any</tspan>
      <tspan x="717" dy="10.5">contractual issues with suppliers,</tspan>
      <tspan x="717" dy="10.5">should they arise. (E.g., You sell</tspan>
      <tspan x="717" dy="10.5">your business, account number</tspan>
      <tspan x="717" dy="10.5">changes, etc.)</tspan>
    </text>
    <text class="step-copy step-copy--end" x="577" y="303">
      <tspan x="577">To protect your business from</tspan>
      <tspan x="577" dy="10.5">market volatility, we contact you</tspan>
      <tspan x="577" dy="10.5">ahead of your contract end date to</tspan>
      <tspan x="577" dy="10.5">discuss renewal options. If anyone</tspan>
      <tspan x="577" dy="10.5">else contacts you, you respond,</tspan>
      <tspan x="577" dy="10.5">“No thank you, we have Brightwell!”</tspan>
    </text>
    <text class="step-copy" x="825" y="319">
      <tspan x="825">Sleep Easy! You'll never fall</tspan>
      <tspan x="825" dy="10.5">“out of contract” with</tspan>
      <tspan x="825" dy="10.5">Brightwell as your broker.</tspan>
    </text>
  </g>

  <!-- step badges -->
  <g class="badges">
    <!-- 01 review -->
    <g transform="translate(672,660)">
      <rect class="badge-shape" x="-22" y="-22" width="44" height="44" rx="9" transform="rotate(45)"/>
      <rect class="badge-icon" x="-9" y="-11" width="16" height="21" rx="1.5"/>
      <circle class="badge-icon" cx="0" cy="1" r="5"/>
      <path class="badge-icon" d="M4,5 L10,11"/>
    </g>
    <!-- 02 options -->
    <g transform="translate(177,548)">
      <rect class="badge-shape" x="-22" y="-22" width="44" height="44" rx="9" transform="rotate(45)"/>
      <circle class="badge-icon" cx="-8" cy="-8" r="3"/>
      <circle class="badge-icon" cx="0" cy="-8" r="3"/>
      <circle class="badge-icon" cx="8" cy="-8" r="3"/>
      <path class="badge-icon" d="M-8,-5 L0,3 M0,-5 L0,3 M8,-5 L0,3 M0,3 L0,12"/>
    </g>
    <!-- 03 sign-up -->
    <g transform="translate(782,548)">
      <rect class="badge-shape" x="-22" y="-22" width="44" height="44" rx="9" transform="rotate(45)"/>
      <rect class="badge-icon" x="-9" y="-11" width="15" height="21" rx="1.5"/>
      <path class="badge-icon" d="M-6,-5 H3 M-6,-1 H3 M-6,3 H0 M10,-6 L10,9 L8,12"/>
    </g>
    <!-- 04 quality check -->
    <g transform="translate(285,438)">
      <rect class="badge-shape" x="-22" y="-22" width="44" height="44" rx="9" transform="rotate(45)"/>
      <rect class="badge-icon" x="-11" y="-10" width="22" height="18" rx="2"/>
      <circle class="badge-icon" cx="0" cy="-1" r="4.5"/>
      <path class="badge-icon" d="M-6,12 H6"/>
    </g>
    <!-- 05 monitoring -->
    <g transform="translate(890,438)">
      <rect class="badge-shape" x="-22" y="-22" width="44" height="44" rx="9" transform="rotate(45)"/>
      <rect class="badge-icon" x="-12" y="-10" width="22" height="15" rx="1.5"/>
      <path class="badge-icon" d="M-1,5 V10 M-6,10 H4"/>
      <circle class="badge-icon" cx="2" cy="-3" r="4"/>
      <path class="badge-icon" d="M5,0 L10,5"/>
    </g>
    <!-- 06 renewal protection -->
    <g transform="translate(397,326)">
      <rect class="badge-shape" x="-22" y="-22" width="44" height="44" rx="9" transform="rotate(45)"/>
      <circle class="badge-icon" cx="0" cy="0" r="11"/>
      <path class="badge-icon" d="M0,-7 L6,-4 V1 Q6,6 0,8 Q-6,6 -6,1 V-4 Z"/>
      <path class="badge-icon" d="M-3,0 L-1,2.5 L3,-2"/>
    </g>
    <!-- 07 guarantee -->
    <g transform="translate(1002,326)">
      <rect class="badge-shape" x="-22" y="-22" width="44" height="44" rx="9" transform="rotate(45)"/>
      <path class="badge-icon" d="M-10,-9 l1.5,3 3,0.4 -2.2,2 0.6,3 -2.9,-1.5 -2.9,1.5 0.6,-3 -2.2,-2 3,-0.4 Z"/>
      <path class="badge-icon" d="M4,-9 l1.5,3 3,0.4 -2.2,2 0.6,3 -2.9,-1.5 -2.9,1.5 0.6,-3 -2.2,-2 3,-0.4 Z"/>
      <path class="badge-icon" d="M-6,12 V3 H-2 L1,-2 Q3,-2 3,1 V3 H8 Q10,3 9,6 L8,12 Z"/>
    </g>
  </g>

  <!-- headline -->
  <text class="headline" x="1005" y="676">BRIGHTWELL</text>
  <text class="headline" x="1005" y="711">DIFFERENCE</text>
</svg>
</body>
</html>
```